Real Estate Business Cards

Looking for a clean, sharp and professional look for our Real Estate investment Fund that invests in Multi Family Apartment buildings.

Target Market(s)

Real Estate Fund

Industry/Entity Type

Real Estate

Contact Information for Business Card

Company Description: Real Estate Investment Fund
Company Name: RKW Holdings
Name: Marcus Olvane
Cell: (917) 482-0657
Email: marcus@rkwholdings-example.com
Website: www.rkwholdings-example.com
Address: 418, 9th Street, Brooklyn NY 11218

Colors

Designer to choose colors to be used in the design.

Requirements
Nice to have
• Colors to match logo

```html
<!DOCTYPE html>
<html lang="en">
<head>
<meta charset="utf-8">
<title>RKW Holdings – Business Card</title>
<link href="https://fonts.googleapis.com/css2?family=Montserrat:wght@400;600;700&display=swap" rel="stylesheet">
<style>
  :root {
    --page-bg: #e9e9eb;
    --card-black: #0c0c0e;
    --card-dark: #1a1b1e;
    --band: #2a2c30;
    --brand-blue: #3d8fd6;
    --text-light: #e6e7ea;
    --text-muted: #9a9ca2;
    --pill-bg: #16171a;
  }
  * { margin: 0; padding: 0; box-sizing: border-box; }
  html, body {
    width: 1200px; height: 1200px; overflow: hidden;
    background: var(--page-bg);
    font-family: "Montserrat", Arial, sans-serif;
  }
  .card {
    position: absolute; left: 150px;
    width: 900px; height: 514px;
    background: linear-gradient(160deg, var(--card-dark) 0%, var(--card-black) 70%);
    border-radius: 6px;
    box-shadow: 0 18px 40px rgba(0,0,0,0.28);
    overflow: hidden;
  }
  .card--front { top: 60px; }
  .card--back { top: 626px; }

  .card__band {
    position: absolute; left: 0; right: 0;
    background: linear-gradient(180deg, rgba(255,255,255,0.02), var(--band) 50%, rgba(255,255,255,0.02));
  }
  .card--front .card__band { top: 120px; height: 210px; }
  .card--back .card__band { top: 0; height: 150px; }

  .brand { position: absolute; display: flex; align-items: center; gap: 22px; }
  .brand__square { background: var(--brand-blue); border-radius: 3px; }
  .brand__name {
    color: var(--brand-blue); font-weight: 600; letter-spacing: 0.08em;
    text-transform: uppercase; white-space: nowrap;
  }
  .card--front .brand { left: 210px; top: 185px; }
  .card--front .brand__square { width: 70px; height: 70px; }
  .card--front .brand__name { font-size: 46px; }
  .card--back .brand { right: 70px; top: 52px; gap: 16px; }
  .card--back .brand__square { width: 44px; height: 44px; }
  .card--back .brand__name { font-size: 28px; }

  .web-pill {
    position: absolute; left: 50%; top: 380px; transform: translateX(-50%);
    background: var(--pill-bg); color: var(--text-light);
    font-size: 22px; padding: 10px 26px; border-radius: 4px;
    letter-spacing: 0.02em; white-space: nowrap;
  }

  .person { position: absolute; left: 70px; top: 180px; padding-left: 20px; border-left: 4px solid var(--brand-blue); }
  .person__name { color: var(--text-light); font-weight: 700; font-size: 26px; }
  .person__title { color: var(--text-muted); font-size: 21px; margin-top: 4px; }

  .contacts { position: absolute; left: 70px; top: 282px; list-style: none; }
  .contacts li, .address {
    display: flex; align-items: center; gap: 16px;
    color: var(--text-light); font-size: 20px; height: 46px; white-space: nowrap;
  }
  .address { position: absolute; right: 60px; top: 436px; }
  .icon {
    width: 30px; height: 30px; flex: none; border-radius: 50%;
    background: var(--brand-blue);
    display: flex; align-items: center; justify-content: center;
  }
  .icon svg { width: 16px; height: 16px; fill: #fff; }
</style>
</head>
<body>

<section class="card card--front" aria-label="Business card front">
  <div class="card__band"></div>
  <div class="brand">
    <span class="brand__square"></span>
    <span class="brand__name">RKW Holdings</span>
  </div>
  <div class="web-pill">www.rkwholdings-example.com</div>
</section>

<section class="card card--back" aria-label="Business card back">
  <div class="card__band"></div>
  <div class="brand">
    <span class="brand__square"></span>
    <span class="brand__name">RKW Holdings</span>
  </div>

  <div class="person">
    <p class="person__name">Marcus Olvane</p>
    <p class="person__title">President</p>
  </div>

  <ul class="contacts">
    <li>
      <span class="icon"><svg viewBox="0 0 16 16"><path d="M3.5 1.5l2.5 0 1 3.5-1.6 1.2a8 8 0 0 0 4.4 4.4L11 9l3.5 1v2.5c0 1-1 2-2 2A11 11 0 0 1 1.5 3.5c0-1 1-2 2-2z"/></svg></span>
      (917) 482-0657
    </li>
    <li>
      <span class="icon"><svg viewBox="0 0 16 16"><path d="M1 3.5h14v9H1z M1.5 4l6.5 5 6.5-5" fill="none" stroke="#fff" stroke-width="1.6"/></svg></span>
      marcus@rkwholdings-example.com
    </li>
    <li>
      <span class="icon"><svg viewBox="0 0 16 16"><g fill="none" stroke="#fff" stroke-width="1.4"><circle cx="8" cy="8" r="6.5"/><ellipse cx="8" cy="8" rx="2.8" ry="6.5"/><path d="M1.5 8h13"/></g></svg></span>
      www.rkwholdings-example.com
    </li>
  </ul>

  <p class="address">
    <span class="icon"><svg viewBox="0 0 16 16"><path d="M8 1a5 5 0 0 1 5 5c0 3.5-5 9-5 9S3 9.5 3 6a5 5 0 0 1 5-5zm0 3a2 2 0 1 0 0 4 2 2 0 0 0 0-4z"/></svg></span>
    Address: 418, 9th Street, Brooklyn NY 11218
  </p>
</section>

</body>
</html>
```